Business Card Design for Consulting Company

I require a Business Card design for my Consulting company. <br/><br/>My company name is: Marek Olvani Consulting Inc.<br/>My website is: www.marekolvaniconsulting.example<br/><br/>My company focuses on management and software development for the Tallobrix CRM platform (www.tallobrix.example)<br/><br/>I have a logo already designed...see attached.
Updates

Also Include my Name and Title: Marek T.L. Olvani President

Target Market(s)

Tallobrix Customers

Contact Information for Business Card

Only include my LOGO (provided)
My Name: Marek TL Olvani
My Title: President
My Company Name: Marek Olvani Consulting Inc.
My Website: www.marekolvaniconsulting.example
My Email: marek.olvani.consulting@mailbox.example

NO PHONE NUMBER
NO ADDRESS

Font styles to use
Serif
Sans Serif
Other font styles liked:
• see my website: www.marekolvaniconsulting.example

Colors

Designer to choose colors to be used in the design.

Requirements
Must have
• Must include my Orange
• Include my name (Marek T.L. Olvani), title (President) company name, website and email
• It should also have a tag line like: Tallobrix Consulting
• I'm flexible with the tag line
Should not have
• Don't include my phone number or address

```html
<!DOCTYPE html>
<html lang="en">
<head>
<meta charset="utf-8">
<title>Marek Olvani Consulting Inc. — Business Card</title>
<link href="https://fonts.googleapis.com/css2?family=Roboto:wght@400;700&family=Quicksand:wght@500;600&display=swap" rel="stylesheet">
<style>
  :root {
    --backdrop: #232323;
    --card: #0f0f0f;
    --pattern: #151515;
    --orange: #f7891f;
    --white: #f2f2f2;
  }
  * { box-sizing: border-box; margin: 0; padding: 0; }
  html, body { width: 1200px; height: 852px; overflow: hidden; }
  body {
    background: var(--backdrop);
    position: relative;
    font-family: "Roboto", Arial, sans-serif;
  }
  .card {
    position: absolute;
    top: 271px;
    width: 540px;
    height: 309px;
    background: var(--card);
    border-radius: 18px;
    overflow: hidden;
  }
  .card--pattern { left: 45px; }
  .card--details { left: 615px; }

  /* Patterned side */
  .pattern-fill {
    position: absolute;
    inset: 0;
    background: linear-gradient(135deg, var(--pattern), #121212);
  }
  .pattern-brand {
    position: absolute;
    left: 330px;
    top: 118px;
    display: flex;
    align-items: center;
    gap: 8px;
    color: var(--orange);
    font-weight: 700;
    font-size: 13px;
    white-space: nowrap;
  }
  .pattern-brand .brand-mark { width: 22px; height: 22px; }

  /* Details side */
  .brand-mark {
    display: block;
    background: var(--orange);
    flex: none;
  }
  .identity {
    position: absolute;
    left: 40px;
    top: 48px;
    display: flex;
    flex-direction: column;
    align-items: flex-start;
    gap: 10px;
  }
  .identity .brand-mark { width: 62px; height: 62px; }
  .identity-name {
    color: var(--white);
    font-size: 12px;
    font-weight: 400;
    letter-spacing: 0.3px;
    white-space: nowrap;
  }
  .holder {
    position: absolute;
    right: 34px;
    top: 100px;
    text-align: right;
  }
  .holder-name {
    color: var(--orange);
    font-weight: 700;
    font-size: 22px;
    letter-spacing: 0.3px;
    white-space: nowrap;
  }
  .holder-title {
    color: var(--white);
    font-size: 13px;
    margin-top: 3px;
  }
  .divider {
    position: absolute;
    left: 40px;
    right: 30px;
    top: 188px;
    height: 1.5px;
    background: var(--orange);
  }
  .contacts {
    position: absolute;
    left: 40px;
    top: 206px;
    list-style: none;
    font-family: "Quicksand", Arial, sans-serif;
    font-weight: 600;
    color: var(--white);
    font-size: 16px;
  }
  .contacts li {
    display: flex;
    align-items: center;
    gap: 10px;
    margin-bottom: 16px;
    white-space: nowrap;
  }
  .contacts svg { flex: none; }
</style>
</head>
<body>
  <section class="card card--pattern" aria-label="Card patterned side">
    <div class="pattern-fill" role="img" aria-label="Faint repeating brand pattern in dark grey"></div>
    <div class="pattern-brand"><span class="brand-mark"></span>Marek Olvani Consulting Inc.</div>
  </section>

  <section class="card card--details" aria-label="Card details side">
    <div class="identity">
      <span class="brand-mark"></span>
      <p class="identity-name">Marek Olvani Consulting Inc.</p>
    </div>

    <div class="holder">
      <p class="holder-name">Marek T.L. Olvani</p>
      <p class="holder-title">President</p>
    </div>

    <div class="divider"></div>

    <ul class="contacts">
      <li>
        <svg width="15" height="12" viewBox="0 0 14 11" aria-hidden="true">
          <rect x="0.5" y="0.5" width="13" height="10" rx="1.5" fill="var(--orange)"/>
          <path d="M2 2.5 L7 6.5 L12 2.5" stroke="var(--card)" stroke-width="1.4" fill="none"/>
        </svg>
        marek.olvani.consulting@mailbox.example
      </li>
      <li>
        <svg width="15" height="15" viewBox="0 0 14 14" aria-hidden="true">
          <circle cx="7" cy="7" r="6.5" fill="var(--orange)"/>
          <path d="M1 7 H13 M7 0.5 C4 4 4 10 7 13.5 M7 0.5 C10 4 10 10 7 13.5" stroke="var(--card)" stroke-width="1" fill="none"/>
        </svg>
        www.marekolvaniconsulting.example
      </li>
    </ul>
  </section>
</body>
</html>
```